Theatre Event Email Invite - Gold Lion over Theatre Interior (Reference images attached)

I need an email invitation to my theatre event.

Design:
Please design a graphic gold lion mask similar to the image attached.
Place it over the red image attached of the theatre's interior
Place the following text over it, in gold font:

"
December 15, 2015 at 7 PM
You are cordially invited to an innovative theatrical experience.

MENDING THE HARBOR
Winner of the KVW's “Far-Rivers”International Screenplay Competition
Written and directed by Marta Quillen

Hosted by the Gallery Of Daybreak
4127 North Ashgrove Ave, Los Angeles, CA 90481 "

Industry/Entity Type

Movie Theater

Font styles to use
Serif

Requirements
Must have
• The lion mask graphic
• An image of the theatre interior. If you use one other than the red one, please edit to look tinted red.
Nice to have
• jewel tones including gold and burgundy
• dramatic
Should not have
• not be scary or depressing

```html
<!DOCTYPE html>
<html lang="en">
<head>
<meta charset="utf-8">
<title>Mending the Harbor – Invitation</title>
<link href="https://fonts.googleapis.com/css2?family=Cinzel:wght@400;600&family=Crimson+Text:wght@400;600;700&display=swap" rel="stylesheet">
<style>
  :root {
    --gold-dark: #8a6520;
    --gold-mid: #c9a040;
    --gold-light: #f1d67e;
    --gold-text: #f0d990;
    --ink-brown: #3a1f0c;
    --burgundy: #7a1628;
    --burgundy-deep: #4e0c18;
    --hall-dark: #1c0c0a;
    --hall-red: #5a1f18;
  }
  * { margin: 0; padding: 0; box-sizing: border-box; }
  html, body { width: 859px; height: 1200px; overflow: hidden; background: #1a0b08; }
  .invite {
    position: relative;
    width: 859px;
    height: 1200px;
    overflow: hidden;
    font-family: "Crimson Text", Georgia, serif;
  }
  .backdrop { position: absolute; inset: 0; }
  .text {
    position: absolute;
    left: 0;
    width: 100%;
    text-align: center;
    color: var(--gold-text);
  }
  .event-date {
    top: 20px;
    font-weight: 700;
    font-size: 25px;
    letter-spacing: 0.5px;
    color: var(--ink-brown);
  }
  .title-main {
    top: 384px;
    font-family: "Cinzel", "Times New Roman", serif;
    font-size: 44px;
    letter-spacing: 3px;
    color: #e2bd5e;
  }
  .studio {
    top: 511px;
    display: flex;
    justify-content: center;
    align-items: center;
    gap: 10px;
    font-weight: 700;
    font-size: 27px;
    color: var(--ink-brown);
  }
  .studio-dot {
    width: 16px; height: 16px; border-radius: 50%;
    background: var(--ink-brown);
  }
  .welcome { top: 612px; font-size: 31px; line-height: 37px; }
  .title-sub { top: 718px; font-size: 35px; letter-spacing: 1px; }
  .award { top: 766px; font-size: 30px; line-height: 38px; }
  .credit { top: 961px; font-size: 32px; line-height: 37px; }
  .venue { top: 1076px; font-size: 25px; line-height: 34px; }
</style>
</head>
<body>
<main class="invite">
  <svg class="backdrop" width="859" height="1200" viewBox="0 0 859 1200" xmlns="http://www.w3.org/2000/svg">
    <defs>
      <linearGradient id="goldBand" x1="0" y1="0" x2="1" y2="0">
        <stop offset="0" stop-color="var(--gold-dark)"/>
        <stop offset="0.25" stop-color="var(--gold-mid)"/>
        <stop offset="0.5" stop-color="var(--gold-light)"/>
        <stop offset="0.75" stop-color="var(--gold-mid)"/>
        <stop offset="1" stop-color="var(--gold-dark)"/>
      </linearGradient>
      <radialGradient id="velvet" cx="0.5" cy="0.4" r="0.7">
        <stop offset="0" stop-color="var(--burgundy)"/>
        <stop offset="1" stop-color="var(--burgundy-deep)"/>
      </radialGradient>
      <linearGradient id="hall" x1="0" y1="0" x2="0" y2="1">
        <stop offset="0" stop-color="var(--hall-dark)"/>
        <stop offset="0.45" stop-color="var(--hall-red)"/>
        <stop offset="1" stop-color="#6e2a1c"/>
      </linearGradient>
      <radialGradient id="maskGold" cx="0.45" cy="0.4" r="0.6">
        <stop offset="0" stop-color="#e8c45c"/>
        <stop offset="1" stop-color="#9a7226"/>
      </radialGradient>
    </defs>

    <rect class="hall-photo" x="0" y="540" width="859" height="620" fill="url(#hall)" role="img" aria-label="Photograph of a theatre interior with rows of seats, tinted red"/>

    <rect class="velvet-field" x="0" y="0" width="859" height="480" fill="url(#velvet)" role="img" aria-label="Burgundy damask pattern background"/>

    <path class="band-top" d="M0 0 H859 V56 L600 56 L430 84 L259 56 L0 56 Z" fill="url(#goldBand)"/>

    <circle class="lion-mask" cx="430" cy="182" r="116" fill="url(#maskGold)" stroke="#d8b45a" stroke-width="4" role="img" aria-label="Gold lion mask emblem"/>

    <path class="band-mid" d="M0 456 L259 456 L430 438 L600 456 L859 456 V560 L600 560 L430 580 L259 560 L0 560 Z" fill="url(#goldBand)"/>

    <circle class="award-seal" cx="430" cy="893" r="44" fill="none" stroke="#d9b552" stroke-width="4"/>

    <rect class="band-bottom" x="0" y="1146" width="859" height="54" fill="url(#goldBand)"/>
  </svg>

  <p class="text event-date">DECEMBER 15, 2015 AT 7 PM</p>
  <h1 class="text title-main">MENDING THE HARBOR</h1>
  <div class="text studio"><span class="studio-dot"></span><span>Larkspur Pictures</span></div>

  <p class="text welcome">You are cordially invited to an innovative<br>theatrical experience.</p>
  <h2 class="text title-sub">MENDING THE HARBOR</h2>
  <p class="text award">Winner of the KVW's “Far-Rivers”International<br>Screenplay Competition</p>
  <p class="text credit">Written and directed by<br>Marta Quillen</p>
  <p class="text venue">Hosted by the Gallery Of Daybreak<br>4127 North Ashgrove Ave, Los Angeles, CA 90481</p>
</main>
</body>
</html>
```